Redesign of existing bottle labels for gin, vodka and rum.

We are a small craft distillery with an existing range of spirits. We would like to "upgrade" our existing branding. Included in the attached file is the current artwork for the range we offer. We would like to retain the brand identity with the following enhancements in mind:
- More focus on the company logo.
- A single adhesion label with 3/4 wrap around and need to have external dimensions of 110mm high x 200mm wide.
- Also attached pictures of the existing bottles, we would like to retain the colored security seal with black top closure at the top. The newly design label should not conflict with this.
The new label should be clean lines and a minimalistic design.
Target Market(s)
Middle to high income professionals. Age group 18 to 65 years. Male and female.
Requirements
Must have
- Clean, minimalistic design
Nice to have
- Modern Feel
Should not have
- Cluttered Design

```html
<!DOCTYPE html>
<html lang="en">
<head>
<meta charset="utf-8">
<title>Kestrelvale Distillery Gin Label</title>
<link href="https://fonts.googleapis.com/css2?family=Oswald:wght@400;500;600&family=Playfair+Display:wght@900&display=swap" rel="stylesheet">
<style>
  :root {
    --backdrop: #e8e9ed;
    --ink: #1e1e1e;
    --ink-soft: #3a3a3a;
    --seal-red: #8e1f25;
    --paper-white: #ffffff;
  }
  * { margin: 0; padding: 0; box-sizing: border-box; }
  html, body {
    width: 1200px;
    height: 1163px;
    overflow: hidden;
    background: var(--backdrop);
  }
  .canvas {
    position: relative;
    width: 1200px;
    height: 1163px;
    font-family: "Oswald", sans-serif;
    color: var(--ink);
  }
  .security-seal {
    position: absolute;
    left: 578px;
    top: 52px;
    width: 44px;
    height: 244px;
    background: var(--seal-red);
    clip-path: polygon(0 0, 100% 0, 100% 100%, 50% 93%, 0 100%);
  }
  .security-seal__text {
    position: absolute;
    left: 50%;
    top: 118px;
    transform: translate(-50%, -50%) rotate(90deg);
    white-space: nowrap;
    color: var(--paper-white);
    font-weight: 500;
    font-size: 15px;
    letter-spacing: 0.5px;
    border-top: 1px solid var(--paper-white);
    border-bottom: 1px solid var(--paper-white);
    padding: 0 2px;
  }
  .label {
    position: absolute;
    left: 0;
    top: 0;
    width: 1200px;
    text-align: center;
  }
  .brand-mark {
    position: absolute;
    left: 565px;
    top: 500px;
    width: 70px;
    height: 70px;
    border-radius: 50%;
    background: var(--ink);
  }
  .brand-name {
    position: absolute;
    left: 0;
    width: 1200px;
    font-weight: 500;
    color: var(--ink);
    text-transform: uppercase;
  }
  .brand-name--main { top: 578px; font-size: 40px; letter-spacing: 1px; line-height: 1; }
  .brand-name--sub { top: 626px; font-size: 15px; letter-spacing: 3px; line-height: 1; }
  .product-name {
    position: absolute;
    left: 0;
    top: 652px;
    width: 1200px;
    font-family: "Playfair Display", serif;
    font-weight: 900;
    font-size: 124px;
    line-height: 1;
    letter-spacing: 4px;
  }
  .origin-heading {
    position: absolute;
    left: 0;
    top: 775px;
    width: 1200px;
    font-size: 17px;
    font-weight: 500;
    line-height: 1;
  }
  .origin-rule {
    position: absolute;
    left: 478px;
    top: 810px;
    width: 204px;
    height: 1px;
    background: var(--ink);
  }
  .origin-country {
    position: absolute;
    left: 524px;
    top: 800px;
    width: 112px;
    height: 19px;
    background: var(--backdrop);
    border: 1px solid var(--ink);
    border-radius: 8px;
    font-size: 13px;
    font-weight: 500;
    line-height: 17px;
    letter-spacing: 1px;
  }
  .origin-by {
    position: absolute;
    left: 0;
    top: 819px;
    width: 1200px;
    font-size: 8px;
    line-height: 1;
    font-weight: 500;
  }
  .origin-maker {
    position: absolute;
    left: 0;
    top: 828px;
    width: 1200px;
    font-size: 14px;
    letter-spacing: 3.4px;
    line-height: 1;
  }
  .style-badge {
    position: absolute;
    left: 484px;
    top: 866px;
    width: 196px;
    height: 31px;
    background: var(--ink);
    border: 2px solid var(--ink);
    outline: 1px solid var(--paper-white);
    outline-offset: -4px;
    color: var(--paper-white);
    font-size: 22px;
    font-weight: 500;
    line-height: 27px;
  }
  .product-story {
    position: absolute;
    left: 484px;
    top: 900px;
    width: 196px;
    font-size: 7.3px;
    line-height: 10.2px;
    font-weight: 500;
    text-align: justify;
    text-align-last: left;
    color: var(--ink-soft);
    text-transform: uppercase;
  }
</style>
</head>
<body>
  <main class="canvas">
    <div class="security-seal">
      <span class="security-seal__text">COLD DISTILLED</span>
    </div>

    <section class="label">
      <span class="brand-mark"></span>
      <p class="brand-name brand-name--main">Kestrelvale</p>
      <p class="brand-name brand-name--sub">Distillery</p>

      <h1 class="product-name">GIN</h1>

      <p class="origin-heading">DISTILLED &amp; BOTTLED</p>
      <span class="origin-rule"></span>
      <p class="origin-country">IN SOUTH AFRICA</p>
      <p class="origin-by">BY</p>
      <p class="origin-maker">KESTRELVALE DISTILLERY</p>

      <p class="style-badge">COLD-DISTILLED GIN</p>
      <p class="product-story">Our handcrafted, small-batch, cold-distilled gin brings together purpose-built equipment, the purest ingredients, finest botanical and passion to produce an unmatched gin worth of your company</p>
    </section>
  </main>
</body>
</html>
```